Kinship Trade Circle Detroit - Honoring Ladies Across Household Ventures

KTC Detroit Spring Workshop, “Honoring Ladies Across Household Ventures.” Discussing how women contribute their vision, energy and wisdom to family businesses. From the C-Suit executives including the “Chief Emotional Officer” to next generations starting in the family business.

Date: Wednesday, May 9, 8:00AM - 10:30AM
Location: RMH
(Networking and continential breakfast starts at 7:30AM)

Investment: Your intelligent questions, positive energy and $75. Includes continential breakfast and parking.

```html
<!DOCTYPE html>
<html lang="en">
<head>
<meta charset="utf-8">
<title>KTC Detroit Spring Workshop</title>
<link rel="stylesheet" href="https://fonts.googleapis.com/css2?family=Didact+Gothic&family=Montserrat:wght@600;700&family=Libre+Franklin:wght@800&family=Libre+Baskerville:wght@700&display=swap">
<style>
  :root {
    --page-bg: #e4e4e4;
    --paper: #ffffff;
    --brand-blue: #2c73b4;
    --brand-blue-light: #5a9bd6;
    --ink: #2e2e2e;
    --ink-soft: #555555;
    --footer-bg: #2a2a2a;
    --dash: #8fb6dc;
  }
  * { margin: 0; padding: 0; box-sizing: border-box; }
  html, body { width: 707px; height: 1200px; overflow: hidden; background: var(--page-bg); }
  .canvas { position: relative; width: 707px; height: 1200px; }
  .flyer {
    position: absolute; left: 30px; top: 141px;
    width: 497px; height: 705px;
    background: var(--paper);
    transform: scale(1.3); transform-origin: top left;
    box-shadow: 0 2px 8px rgba(0,0,0,.25);
    font-family: "Didact Gothic", sans-serif; color: var(--ink);
    text-align: center;
  }
  .brand { position: absolute; top: 10px; left: 0; width: 100%; }
  .brand-name {
    font-family: "Libre Franklin", sans-serif; font-weight: 800;
    font-size: 54px; line-height: 54px; color: var(--brand-blue); letter-spacing: 1px;
  }
  .brand-tagline {
    display: inline-block; margin-top: 6px; padding-top: 3px;
    border-top: 1px solid var(--ink);
    font-family: "Libre Baskerville", serif; font-weight: 700;
    font-size: 8.5px; letter-spacing: .6px; color: var(--ink);
  }
  .brand-sub {
    font-family: "Libre Baskerville", serif; font-size: 5.5px; letter-spacing: .4px;
    color: var(--ink); margin-top: 1px;
  }
  .hero-photo {
    position: absolute; top: 101px; left: 0; width: 100%; height: 254px;
    background: linear-gradient(100deg, #cfdbe4 0%, #e9eef2 35%, #b9c7d2 60%, #dfe6ec 100%);
  }
  .event-kicker {
    position: absolute; top: 367px; width: 100%;
    font-size: 15px; color: var(--ink-soft); letter-spacing: .2px;
  }
  .event-title {
    position: absolute; top: 385px; width: 100%;
    font-family: "Montserrat", sans-serif; font-weight: 700;
    font-size: 22px; line-height: 24px; color: var(--brand-blue); letter-spacing: .3px;
  }
  .event-title .subline { display: block; font-weight: 600; font-size: 17px; line-height: 21px; }
  .event-summary {
    position: absolute; top: 443px; left: 58px; width: 381px;
    font-size: 9px; line-height: 12px; color: var(--ink);
  }
  .event-summary strong { color: var(--brand-blue); font-weight: 700; font-family: "Montserrat", sans-serif; font-size: 8.5px; }
  .venue-box {
    position: absolute; top: 503px; left: 97px; width: 304px; height: 109px;
    border: 1px dashed var(--dash);
  }
  .venue-heading {
    position: absolute; top: -13px; left: 50%; transform: translateX(-50%);
    background: var(--paper); padding: 0 6px;
    font-family: "Montserrat", sans-serif; font-weight: 700; font-size: 20px; line-height: 24px;
    color: var(--brand-blue);
  }
  .venue-line { position: absolute; width: 100%; font-size: 16.5px; color: var(--ink); }
  .venue-line .value { color: var(--brand-blue); }
  .venue-date { top: 15px; }
  .venue-time { top: 40px; }
  .venue-location { top: 63px; }
  .venue-note { position: absolute; top: 90px; width: 100%; font-size: 8.5px; color: var(--ink); }
  .investment { position: absolute; top: 620px; left: 100px; width: 297px; height: 50px; }
  .investment svg { position: absolute; inset: 0; }
  .investment-text {
    position: absolute; top: 9px; width: 100%; color: #fff; font-size: 9.5px; line-height: 11.5px;
  }
  .investment-text .label { font-family: "Montserrat", sans-serif; font-weight: 700; font-size: 9px; }
  .contact-bar {
    position: absolute; top: 675px; left: 0; width: 100%; height: 25px;
    background: var(--footer-bg); color: #fff; font-size: 10px;
    display: flex; align-items: center; justify-content: center; gap: 9px;
  }
  .contact-item { display: flex; align-items: center; gap: 5px; }
  .contact-divider { width: 1px; height: 13px; background: #fff; }
  .contact-icon { width: 12px; height: 12px; }
</style>
</head>
<body>
<div class="canvas">
  <article class="flyer">
    <header class="brand">
      <div class="brand-name">KTC</div>
      <div class="brand-tagline">KINSHIP TRADE CIRCLE DETROIT</div>
      <div class="brand-sub">NETWORK WITH AND LEARN FROM OTHER FAMILY BUSINESSES</div>
    </header>

    <div class="hero-photo" role="img" aria-label="Photo of four businesswomen meeting around a table in a bright office"></div>

    <p class="event-kicker">KTC DETROIT SPRING WORKSHOP</p>
    <h1 class="event-title">HONORING LADIES ACROSS<span class="subline">HOUSEHOLD VENTURES</span></h1>
    <p class="event-summary">Discussing how women contribute their vision, energy and wisdom to family businesses. From the C-Suit executives including the “<strong>Chief Emotional Officer</strong>” to next generations starting in the family business.</p>

    <section class="venue-box">
      <h2 class="venue-heading">VENUE</h2>
      <p class="venue-line venue-date">Date: <span class="value">Wednesday, May 9</span></p>
      <p class="venue-line venue-time">Time:<span class="value">8:00am - 10:30am</span></p>
      <p class="venue-line venue-location">Location: <span class="value">RMH</span></p>
      <p class="venue-note">(Networking and continential breakfast starts at 7:30AM)</p>
    </section>

    <section class="investment">
      <svg width="297" height="50" viewBox="0 0 297 50" aria-hidden="true">
        <defs>
          <linearGradient id="ribbonFill" x1="0" y1="0" x2="0" y2="1">
            <stop offset="0" stop-color="#6aa7de"/>
            <stop offset="1" stop-color="#2a6fb0"/>
          </linearGradient>
        </defs>
        <path d="M8 4 Q10 1 16 1 L291 1 Q296 1 295 6 L289 43 Q288 48 282 48 L6 48 Q1 48 2 43 Z" fill="url(#ribbonFill)"/>
      </svg>
      <div class="investment-text">
        <div class="label">INVESTMENT</div>
        <div>Your intelligent questions, positive energy and $75.</div>
        <div>Includes continential breakfast and parking.</div>
      </div>
    </section>

    <footer class="contact-bar">
      <span class="contact-item">
        <svg class="contact-icon" viewBox="0 0 12 12" aria-hidden="true"><circle cx="6" cy="6" r="5.4" fill="none" stroke="#fff" stroke-width="1"/><path d="M6 2.6a2 2 0 0 1 2 2c0 1.5-2 4-2 4s-2-2.5-2-4a2 2 0 0 1 2-2z" fill="#fff"/></svg>
        KTC Detroit Marian Hollis
      </span>
      <span class="contact-divider"></span>
      <span class="contact-item">
        <svg class="contact-icon" viewBox="0 0 12 12" aria-hidden="true"><circle cx="6" cy="6" r="5.4" fill="none" stroke="#fff" stroke-width="1"/><circle cx="6" cy="6" r="2.8" fill="none" stroke="#fff" stroke-width="1"/><path d="M2.6 6h6.8M6 3.2v5.6" stroke="#fff" stroke-width=".7"/></svg>
        mhollis@hollisadvisory.com
      </span>
      <span class="contact-divider"></span>
      <span class="contact-item">
        <svg class="contact-icon" viewBox="0 0 12 12" aria-hidden="true"><circle cx="6" cy="6" r="5.4" fill="none" stroke="#fff" stroke-width="1"/><path d="M4 3.2l1.2 1.6-.6.8c.4.8 1 1.4 1.8 1.8l.8-.6 1.6 1.2-.7 1c-2.4-.3-4.4-2.3-4.7-4.7z" fill="#fff"/></svg>
        (734) 555-0148
      </span>
    </footer>
  </article>
</div>
</body>
</html>
```